MODERN + COOL Business Card Needed!

SUMMARY
This is for a 40+ year old family business that is transitioning to the 2nd generation and is in real need of a more modern facelift. Ive attached a company logo (I made quickly as an idea with my limited PSD skills) to start off with that you are welcome to change and draw ideas from. Ive also attached some screen shots of cards I like to give you an idea of my preferences.

WHAT WE DO
The company name is Tall Pine HK Ltd. But I prefer to just call it Tall Pine or Tall Pine with Hong Kong as kind of a sub heading on the business card. We own a factory as well as help our customers find factories to make their product. Product I mean, toys 99.9% of the time. Simple old school toys like board games, puzzles, wooden toys, baby/infant toys.

You can say we are a "sourcing" or "trading" or "consulting" company with a factory to help you do it. But since we deal with toys, i like to keep it modern and cool and fun, not serious like managing hedge funds.

WHAT WE ARE LOOKING FOR
A cool, unique looking business card that stands out. In terms of design, something modern and professional. I like darker colored cards and I like colors such as blue/green/dark gray, but am open to other colored themes. I Like bright lime green with gray, always though thats a nice combo. I prefer cards that are all colored and not so much white showing (I think). Ive attached a few screenshots of cards so take a look to get a feel of what I like.

We do alot of wooden stacking games in variety of colors too like Tovra, Lumo, Towerplix (google these to check them out). So designs that sort of resemble stacking or building would be cool but totally not necessary.

In terms of the physical aspects of the card, Im looking for a card a bit different than the standard rectangular shape. Double sided. Little things like having corner(s) be round or different angle instead of square edge I always thought was nice. Its got to be mostly a normal card size, no folding or smaller cards that fit weird in your wallet. No vertical designs. Am open to VERY different/creative shapes (as long as it still fits in a wallet good like a normal buisness card.
Updates

Hi everyone!

Just wanted to write a message to everyone to let them know all submissions are being reviewed or have been reviewed.  If I have not responded with feedback, rest assure your submission was definitely looked at in detail but I either have just been too busy to respond (alot of submissions!), or its on my to be considered list.

I respect and really enjoy receiving everyones creativity and work so I dont want it to go unrecognized - thus this message!  Feel free to submit more ideas if you like until this project ends.  Sometimes some designs just dont click but sometimes they can so you never know!

Thanks again for everyones participation and great work!

~Dev Orr

Target Market(s)

The cards are mainly handed to toy company sourcers and buyers. People I talk to ... say Pelvane for example... might want to make their next edition of Farthingale game with a reputable factory at a good cost so they can sell it to stores at a profit.

So these are the types of people I often try to talk and introduce myself and my company to.

Industry/Entity Type

Building

Colors
acd036
0392cd
00a88e
474747
606060

Requirements
Must have
• Just double sided, not plain rectangle corners, and just cool to look at and catches your eye!

Oh and the obvious business card stuff like place for name, address, number, email, etc.
Nice to have
• Think more modern and fun, not serious and old fashion (thats what we used to be!). Can use the logo I attached and you can definitely alter and change the logo or make a whole new one!

Oh and can definitely use a creative slogan if you like to think of one based on what I described in what we do.
Should not have
• Dont use fonts or text placement that might make "Tall Pine" look like "Tal Lpine"... We arent selling news papers!!

Please nothing related to education since we have the word Pine in the title, thats not our business at all.

Logo and design should not be too heavy on things related to toys, as though thats what we primarily focus on now, what we do may change over time.

```html
<!DOCTYPE html>
<html lang="en">
<head>
<meta charset="utf-8">
<title>Tall Pine – Business Card</title>
<link rel="stylesheet" href="https://fonts.googleapis.com/css2?family=Mulish:wght@400;600;700&display=swap">
<style>
  :root {
    --backdrop: #3d3d3d;
    --card-black: #0b0b0b;
    --card-glow: #262626;
    --lime: #9acd00;
    --text-light: #d6d6d6;
  }
  html, body {
    margin: 0;
    padding: 0;
    width: 1200px;
    height: 900px;
    overflow: hidden;
    background: var(--backdrop);
  }
  .canvas {
    position: relative;
    width: 1200px;
    height: 900px;
    font-family: "Mulish", "Century Gothic", sans-serif;
  }
  .card {
    position: absolute;
    left: 150px;
    top: 200px;
    width: 900px;
    height: 500px;
    border-radius: 52px 0 52px 0;
    background:
      radial-gradient(ellipse 520px 360px at 560px 250px, var(--card-glow) 0%, rgba(38,38,38,0) 100%),
      var(--card-black);
    overflow: hidden;
  }
  .card__bands {
    position: absolute;
    left: 0;
    top: 0;
    width: 900px;
    height: 500px;
    filter: drop-shadow(8px 6px 10px rgba(0,0,0,0.75));
  }
  .card__band {
    fill: var(--lime);
  }
  .brand {
    position: absolute;
    left: 316px;
    top: 136px;
    width: 170px;
    text-align: center;
    margin: 0;
    font-size: 31px;
    font-weight: 600;
    letter-spacing: 0.2px;
    color: var(--lime);
    line-height: 1;
  }
  .contact {
    position: absolute;
    right: 116px;
    top: 272px;
    text-align: right;
  }
  .contact__name {
    margin: 0 0 6px;
    font-size: 44px;
    font-weight: 700;
    color: var(--lime);
    line-height: 1.05;
    letter-spacing: 0.5px;
  }
  .contact__line {
    margin: 0;
    font-size: 19px;
    font-weight: 400;
    color: var(--text-light);
    line-height: 27px;
    letter-spacing: 0.4px;
  }
</style>
</head>
<body>
  <main class="canvas">
    <section class="card" aria-label="Tall Pine business card">
      <svg class="card__bands" viewBox="0 0 900 500" aria-hidden="true">
        <polygon class="card__band" points="108,0 176,0 296,500 228,500"/>
        <polygon class="card__band" points="-130,0 -60,0 110,500 40,500"/>
      </svg>
      <p class="brand">Tall Pine</p>
      <div class="contact">
        <h1 class="contact__name">Ray Dunmore</h1>
        <p class="contact__line">999.555.4821</p>
        <p class="contact__line">Ray@tallPINE.com</p>
        <p class="contact__line">www.tallPINE.com</p>
      </div>
    </section>
  </main>
</body>
</html>
```